Web Design for New Antenna Company that is ready to revolutionize World Wide Communicaitons

This is the task description that I used for the Logo, please us it as a reference for the “message” of the company.

The name of the Company is "Verdant Arc Incorporated". We build highly efficient antennas that make a direct connection between communication points that make use of highly focus radio beams that support extremely high data rates (wireless internet) over the air.

The reference used for, antenna gain (the measure of an antennas' ability to focus/concentrate energy (radio energy) into a beam is measured by the antennas gain, which uses the Unit vAi, (decibels relative to an isotropic), and these are the initials of our corporate name. Antennas of high gain are focused like a laser, while the reference (isotropic) is a sphere or ball, radiating equally in all directions. The earth is a sphere. Think of Global Communications, as we will offer our products to all parts of the Globe, connecting people with vital information.

I like the feeling of "Direct" as it is definitive, and the idea of the "Beam" in that it carries information, so the main message is contained in the first two words "Verdant Arc" and Incorporated completes the idea and ties to the reference "vAi".

Our tag lines is: "Setting the standard for communications"

I have some 3D antenna patterns (shape of the energy in a 3 dimensional rendering). The colors that are chosen for the rainbow scale are, from most intense to lower intensity, red, sliding through orange to yellow, followed by green and then blue. I also like black for strong contrast. The radiated beam could be outlined in a strong color like black or blue, with a orange/red core color denoting temperature or intense heat (high energy / plasma). My thought of a logo would be a simple but strong image that somehow brings together the descriptions given above, possibly with a intense "beam" as described and possibly in the colors described, as long as the image does not get too "busy" or complex.

Don't feel confined by the use of any particular colors, just use your imagination and see if there is a simple strong image that brings the message home.

Thanks, I appreciate your ideas and look forward to seeing your work.

Regards,

Tam

I have files to share from the previous LOGO design, including EPS files for your use.

Thank you for your interest in providing a website for me.

Also find...

Please find the enclosed links to 3 website that I like, that are in my industry, which is Business to Business in Communications, both Government and Commercial.

Hopefully you can make use of reusing code, so please find something that fits the simple needs that I have.

The first looks too simple for me. The Graphics are too simple, with solid colors, and not too interesting.
http://pwaerials.example/

The second is Kellam Corporation is probably over the top, with the main graphics fanning out to each side. This is a nice effect, but not at all necessary.

I like to top “ribbon” selection” that open into outlined in solid color, filled rounded rectangles. It has a solid look. ( HOME COMPANY MARKETS/SOLUTIONS….)

I like the single page, with information on the bottom of the page, so you do not have to drill down to see what they are about.
http://kellam.example/

The following is probably the closest to what I may really need. This is smaller company, certainly smaller than Kellam, but not so personal as the smallest PW, that includes the designers resume.
http://www.mkfluxon.example/

I like the top of the site to resemble our Business Cards, Letterhead, showing our Logo with full Globe Background, (EPS file) which is enclosed in this mail.

I want to look like a serious company, displaying decades of experience, helping to build our Global Wireless communication system, that we all enjoy today.

I will be writing a Mission Statement, that will be included in the About US, or History Section. I would like to have an area for testimonials, as I have offers from some significant companies that would be happy to provide feedback on our design capabilities.

HOME About US, Markets/Solutions Products/Services

I like that the areas above, when hovered show the pull down without having to actually select the item.

I will enclose, if you send me your e-mail the files to assist... "my favorite" is the Logo, that I like best. I think that the lines and continents on the Globe need to be brought out better so they can be seen. I am including the source files (.eps & .rar)

I will be glad to include other JPEGs of logos that are of different colors on white background. The "tag line" under the name should always be "Setting the Standard for Communications" and not "We set..."

Thanks for your help. I look forward to your proposals Please do not hesitate to call.

Regards,

Tam

Cell # 555-271-9034
tamholt@verdantarcinc.example

I do have files (eps, rar) files for the logo design that I would like used in the website.
Please send an e-mail request at: tamholt@verdantarcinc.example and I will forward them to you.

I can also send you the brief, that was used for the LOGO request, that may provide insight to
the type of message that I want to convey.

Thanks,

Tam

Reason: I am extending to allow enough time so that we are not rushed.

```html
<!DOCTYPE html>
<html lang="en">
<head>
<meta charset="utf-8">
<title>Verdant Arc Incorporated</title>
<link href="https://fonts.googleapis.com/css2?family=Source+Sans+3:wght@300;400;600;700&family=Bitter:wght@400;700&display=swap" rel="stylesheet">
<style>
:root{
  --canvas:#eceef1;
  --page:#ffffff;
  --ink:#2b2e33;
  --muted:#8b9097;
  --line:#e4e6e9;
  --accent:#3b8fd6;
  --hero-panel:#2a2f37;
  --blue-deep:#2f74b4;
  --blue-bright:#4a9be0;
  --blue-soft:#6fa8da;
  --link:#2e7cc3;
}
*{margin:0;padding:0;box-sizing:border-box}
html,body{width:1094px;height:1200px;overflow:hidden}
body{background:var(--canvas);font-family:"Source Sans 3",sans-serif;color:var(--ink);position:relative}
.page{position:absolute;left:249px;top:9px;width:596px;height:1063px;background:var(--page);box-shadow:0 0 3px rgba(0,0,0,.08)}
.abs{position:absolute}
.top-stripe{left:207px;top:0;width:376px;height:3px;background:repeating-linear-gradient(90deg,#5aa2dc 0 4px,#82baea 4px 6px)}
.brand{display:flex;align-items:center;gap:8px;font:600 22px/1 "Source Sans 3",sans-serif;color:var(--ink);white-space:nowrap}
.brand-dot{width:14px;height:14px;border-radius:50%;background:var(--accent);flex:none}
.social{display:flex;gap:7px;align-items:center}
.social i{display:block;width:5px;height:5px;border-radius:50%;background:#4b4f56}
.meta{font-size:8px;color:var(--link);display:flex;align-items:center;gap:5px;white-space:nowrap}
.meta-divider{width:1px;height:28px;background:var(--line)}
.nav{display:flex;font-size:10px;color:#3a3d42;align-items:center;white-space:nowrap}
.nav span{padding:0 6px}
.nav .current{color:var(--accent)}
.nav .boxed{border:1px solid #dfe2e6;padding:5px 11px;margin:0 2px}
.caret{font-size:6px;color:#9aa0a7;padding:0 2px 0 0!important}
.photo{display:block}
.hero-photo{left:12px;top:79px;width:286px;height:205px;background:linear-gradient(180deg,#1e3a6e 0%,#4c6fa8 45%,#8ea6c2 68%,#2f4a2a 80%,#4d7a2e 100%)}
.hero-panel{left:298px;top:79px;width:285px;height:205px;background:var(--hero-panel)}
.hero-title{left:13px;top:28px;font:400 27px/29px "Source Sans 3",sans-serif;color:#fff;letter-spacing:.2px;white-space:nowrap}
.btn{display:inline-flex;align-items:center;gap:10px;font:700 8px "Source Sans 3",sans-serif;letter-spacing:.2px;padding:0 9px;height:22px;border:1px solid;white-space:nowrap}
.btn-dark{border-color:#5d636c;color:#a9afb8}
.btn-light{border-color:rgba(255,255,255,.55);color:#fff}
.tile-label{font-size:8px;color:rgba(255,255,255,.7);letter-spacing:.2px}
.tile-title{font:400 17px/16px "Source Sans 3",sans-serif;color:#fff;text-transform:uppercase;margin-top:3px}
.heading{font:700 14px "Bitter",serif;color:var(--ink)}
.heading em{font-style:normal;font-weight:400;color:#8a9099}
.contact-label{font-size:7px;color:#9aa0a6}
.contact-row{display:flex;gap:6px;align-items:flex-start;font-size:8px;color:#3a3d42;line-height:10px}
.contact-row.link{color:var(--link)}
.hr{height:1px;background:var(--line)}
.offer-a{font:700 19px/1 "Bitter",serif;color:var(--accent)}
.offer-b{font:700 27px/1 "Bitter",serif;color:var(--ink)}
.card{width:144px;height:122px;text-align:center;box-shadow:inset 1px 0 0 #f1f2f4,inset -1px 0 0 #f1f2f4}
.card .product-shot{width:54px;height:48px;margin:6px auto 0;border-radius:3px;background:linear-gradient(160deg,#3c4047,#0e1013)}
.card h4{font:400 11px "Source Sans 3",sans-serif;margin-top:10px;color:#2b2e33}
.card p{font-size:7.5px;line-height:11px;color:#9aa0a6;margin:4px 10px 0}
.col{width:142px;height:124px;padding:8px 8px 0;box-shadow:inset -1px 0 0 #f0f1f3}
.col h3{font:700 12px "Bitter",serif;color:var(--ink)}
.col h3 em{font-style:normal;font-weight:400;color:#8a9099}
.small{font-size:7.5px;line-height:10px}
.post{display:flex;gap:7px;margin-top:10px}
.thumb{width:32px;height:29px;background:linear-gradient(#d7d9dc,#b9bcc0);position:relative;flex:none}
.thumb b{position:absolute;left:3px;bottom:0;width:10px;height:8px;background:var(--accent)}
.date{font-size:6px;color:#b0b4b9;margin-top:3px}
.tweet{display:flex;gap:6px;margin-top:10px}
.tweet a{color:var(--link);font-style:italic}
.arrow-btn{width:19px;height:18px;border:1px solid #d6d9dd;display:flex;align-items:center;justify-content:center;color:var(--accent);font-size:9px}
.hatch{left:12px;top:923px;width:571px;height:6px;background:repeating-linear-gradient(135deg,#e3e5e8 0 1px,transparent 1px 3px)}
.copyright{left:0;top:1035px;width:596px;text-align:center;font-size:7px;color:#6d7279}
</style>
</head>
<body>
<div class="page">
  <div class="abs top-stripe"></div>
  <div class="abs brand" style="left:14px;top:29px"><span class="brand-dot"></span>Verdant Arc</div>

  <div class="abs social" style="left:233px;top:18px"><i></i><i></i><i></i><i></i><i></i><i></i><i></i><i></i><i></i></div>
  <div class="abs meta-divider" style="left:364px;top:6px"></div>
  <div class="abs meta" style="left:380px;top:16px">
    <svg width="9" height="9" viewBox="0 0 10 10"><path d="M2 1l2 2-1 1.5c.6 1.3 1.3 2 2.5 2.5L7 6l2 2-1.5 1.5C4.5 9 1 5.5.5 2.5z" fill="#2b2e33"/></svg>+555-271-9034</div>
  <div class="abs meta-divider" style="left:464px;top:6px"></div>
  <div class="abs meta" style="left:479px;top:16px">
    <svg width="9" height="7" viewBox="0 0 10 8"><rect x=".5" y=".5" width="9" height="7" fill="none" stroke="#2b2e33"/><path d="M.5.5l4.5 4 4.5-4" fill="none" stroke="#2b2e33"/></svg>contact@vai.example</div>

  <nav class="abs nav" style="right:7px;top:48px">
    <span class="current">Home</span><span>About US</span><span>Products</span><span class="caret">▾</span><span>Markets</span><span class="boxed">Portfolio</span><span>News</span><span>Contact</span>
  </nav>

  <div class="abs photo hero-photo" role="img" aria-label="Satellite dish antennas at dusk"></div>
  <div class="abs hero-panel">
    <div class="abs hero-title">SETTING THE<br>STANDARD FOR<br>COMMUNICATIONS</div>
    <div class="abs" style="left:15px;top:147px"><span class="btn btn-dark">READ MORE <span>→</span></span></div>
  </div>

  <div class="abs photo" role="img" aria-label="Glowing globe with network lines" style="left:12px;top:297px;width:142px;height:119px;background:radial-gradient(circle at 45% 50%,#7fbef0,#1d5fa8 55%,#0d2f63)"></div>
  <div class="abs" style="left:154px;top:297px;width:144px;height:119px;background:var(--blue-deep);padding:14px 10px">
    <div class="tile-label">INTERESTING INFO</div>
    <div class="tile-title">Some<br>valuable<br>information</div>
    <div style="margin-top:8px"><span class="btn btn-light">READ MORE <span>→</span></span></div>
  </div>
  <div class="abs photo" role="img" aria-label="Businessman in front of an office building" style="left:298px;top:297px;width:142px;height:119px;background:linear-gradient(90deg,#c9d0d8,#9aa4b0 40%,#2a2d33 60%,#b7bfc8)"></div>
  <div class="abs" style="left:440px;top:297px;width:143px;height:119px;background:var(--blue-bright);padding:14px 10px">
    <div class="tile-label">VERY IMPORTNAT</div>
    <div class="tile-title">Did you<br>know ?</div>
    <div style="margin-top:24px"><span class="btn btn-light">READ MORE <span>→</span></span></div>
  </div>

  <div class="abs photo" role="img" aria-label="Network cabling in server racks" style="left:12px;top:428px;width:142px;height:96px;background:linear-gradient(135deg,#3f6f62,#7fb3b0 50%,#2c3238)"></div>
  <div class="abs photo" role="img" aria-label="Blue lit data center aisle" style="left:154px;top:428px;width:144px;height:96px;background:radial-gradient(circle at 50% 55%,#6fb4ff,#1743a0 55%,#071430)"></div>
  <div class="abs photo" role="img" aria-label="Communication tower against the sky" style="left:12px;top:524px;width:142px;height:97px;background:linear-gradient(180deg,#cfe2f2,#8fb5d6 60%,#3d5366)"></div>
  <div class="abs" style="left:154px;top:524px;width:144px;height:97px;background:var(--blue-soft);padding:15px 15px">
    <div class="tile-title" style="font-size:17px">Our latest<br>projects</div>
    <div style="margin-top:9px"><span class="btn btn-light">CHECK ALL <span>→</span></span></div>
  </div>

  <div class="abs" style="left:305px;top:427px;width:130px">
    <div class="heading">Contact <em>with us</em></div>
    <div class="contact-label" style="margin-top:8px">phone number</div>
    <div class="contact-row" style="margin-top:6px;font-size:10px;color:#1f3f66"><svg width="9" height="9" viewBox="0 0 10 10"><path d="M2 1l2 2-1 1.5c.6 1.3 1.3 2 2.5 2.5L7 6l2 2-1.5 1.5C4.5 9 1 5.5.5 2.5z" fill="#2b2e33"/></svg>+555-271-9034</div>
    <div class="hr" style="margin-top:8px"></div>
    <div class="contact-label" style="margin-top:6px">our address</div>
    <div class="contact-row" style="margin-top:6px"><svg width="8" height="10" viewBox="0 0 8 10"><path d="M4 0a3.5 3.5 0 013.5 3.5C7.5 6 4 10 4 10S.5 6 .5 3.5A3.5 3.5 0 014 0z" fill="#2b2e33"/><circle cx="4" cy="3.5" r="1.3" fill="#fff"/></svg><span>Some address goes here including street, city and country</span></div>
    <div class="hr" style="margin-top:8px"></div>
    <div class="contact-label" style="margin-top:8px">e-mail address</div>
    <div class="contact-row link" style="margin-top:7px"><svg width="9" height="7" viewBox="0 0 10 8"><rect x=".5" y=".5" width="9" height="7" fill="none" stroke="#2b2e33"/><path d="M.5.5l4.5 4 4.5-4" fill="none" stroke="#2b2e33"/></svg>contact@vai.example</div>
    <div class="hr" style="margin-top:6px"></div>
    <div class="contact-label" style="margin-top:4px">twitter</div>
    <div class="contact-row link" style="margin-top:7px"><svg width="8" height="8" viewBox="0 0 8 8"><path d="M1 1l6 3-6 3 1.5-3z" fill="#2b2e33"/></svg>@vai.example</div>
  </div>
  <div class="abs photo" role="img" aria-label="Street map with location marker" style="left:440px;top:429px;width:143px;height:192px;background:linear-gradient(135deg,#ebe6d6,#f3edd9 45%,#a9c4e6 70%,#eae4d2)"></div>

  <div class="abs offer-a" style="left:31px;top:661px">What we</div>
  <div class="abs offer-b" style="left:55px;top:678px">offer:</div>
  <div class="abs card" style="left:154px;top:635px"><div class="product-shot" role="img" aria-label="Product A unit"></div><h4>Product A</h4><p>Donec id iaculis massa. Class aptent taciti sociosqu ad ...</p></div>
  <div class="abs card" style="left:298px;top:635px"><div class="product-shot" role="img" aria-label="Product B unit"></div><h4>Product B</h4><p>Donec id iaculis massa. Class aptent taciti sociosqu ad ...</p></div>
  <div class="abs card" style="left:440px;top:635px"><div class="product-shot" role="img" aria-label="Product C unit"></div><h4>Product C</h4><p>Donec id iaculis massa. Class aptent taciti sociosqu ad ...</p></div>

  <div class="abs col" style="left:12px;top:792px">
    <h3>About <em>us:</em></h3>
    <p class="small" style="margin-top:7px;font-weight:600">Nulla ipsum dolor lacus, suscipit adipiscing. Cum sociis natoque.</p>
    <p class="small" style="margin-top:4px;color:var(--muted)">Nullam wisi ultricies a, gravida vitae, dapibus risus ante sodales lectus blandit eu, tempor diam</p>
    <div style="margin-top:9px;margin-left:52px"><span class="btn" style="border-color:#d6d9dd;color:var(--link);height:19px">READ MORE <span>→</span></span></div>
  </div>
  <div class="abs col" style="left:156px;top:792px">
    <h3>Latest <em>posts:</em></h3>
    <div class="post"><div class="thumb"><b></b></div><div><p class="small" style="font-weight:600">Nullam wisi ultricies a, gravida vitae</p><p class="date">▦ October 04, 2012</p></div></div>
    <div class="post"><div class="thumb"><b></b></div><div><p class="small" style="font-weight:600">Nullam wisi ultricies a, gravida vitae</p><p class="date">▦ October 04, 2012</p></div></div>
  </div>
  <div class="abs col" style="left:298px;top:792px">
    <h3>Twitter:</h3>
    <div class="tweet"><svg width="8" height="8" viewBox="0 0 8 8" style="flex:none;margin-top:1px"><path d="M1 1l6 3-6 3 1.5-3z" fill="#2b2e33"/></svg><div class="small"><b style="font-weight:600">Suspendisse a pellentesque dui non felis</b><br><a>http://example.com/DGERTAE</a><br><span style="color:var(--muted);font-size:6.5px">23 hours ago</span></div></div>
    <div class="tweet"><svg width="8" height="8" viewBox="0 0 8 8" style="flex:none;margin-top:1px"><path d="M1 1l6 3-6 3 1.5-3z" fill="#2b2e33"/></svg><div class="small"><b style="font-weight:600">Vestibulum commodo volutpat</b><br><a>http://example.com/DGERTAE</a><br><span style="color:var(--muted);font-size:6.5px">23 hours ago</span></div></div>
  </div>
  <div class="abs col" style="left:440px;top:792px;box-shadow:none">
    <h3><em>Our</em> clients:</h3>
    <div style="display:flex;align-items:center;gap:5px;margin:26px 0 0 16px;font-size:17px;color:#2b2e33"><span style="width:17px;height:17px;background:#c8202c;display:block"></span>Northpeak</div>
    <div style="display:flex;gap:4px;margin:22px 0 0 50px"><div class="arrow-btn">←</div><div class="arrow-btn">→</div></div>
  </div>

  <div class="abs hatch"></div>
  <div class="abs social" style="left:19px;top:940px"><i></i><i></i><i></i><i></i><i></i><i></i><i></i><i></i><i></i></div>
  <nav class="abs nav" style="right:12px;top:937px;font-size:7.5px;color:#6d7279">
    <span class="current">HOME</span><span style="padding:0 9px">About US</span><span style="padding:0 9px">Products</span><span style="padding:0 9px">Markets</span><span style="padding:0 9px">Portfolio</span><span style="padding:0 9px">News</span><span style="padding-right:0">Contact</span>
  </nav>
  <div class="abs brand" style="left:0;width:596px;justify-content:center;top:982px;font-size:20px"><span class="brand-dot" style="width:12px;height:12px"></span>Verdant Arc</div>
  <div class="abs copyright">© 2013 Verdant Arc - All Rights Reserved.</div>
</div>
</body>
</html>
```